Marwell Herd Services concrete grooving services flyer design

Marwell Herd Services offers 4 different grooving options:

DEEP GROOVING
, ideal for Safety & Efficiency
Our hugely popular deep straight line grooving, long lasting, minimal hoof wear,

Create safe and secure flooring, cows walk without hesitation

Achieve groove spacing for optimal hoof function, reduce hoof trauma

Ideal grooves to new concrete or surfaces with little to no pattern or previous grooving

Ideal groove pattern as promoted by The pasturewide programme

MINI GROOVING,
Smaller dimensions Ideal option for heifer housing and high activity areas such as parlours and handling areas

An ideal solution for regaining traction on old previous grooving that has lost its traction without loosing stability

Plaining

smoothing down rough concrete with previous aggressive grooving or patterns to reduce hoof trauma & wear

SENSOR PLATE SINKING

sinking sensor plates for automated machines below surface level preventing accidental damage & wear

```html
<!DOCTYPE html>
<html lang="en">
<head>
<meta charset="utf-8">
<title>Marwell Herd Services – Concrete Grooving</title>
<link rel="stylesheet" href="https://fonts.googleapis.com/css2?family=Bebas+Neue&family=Manrope:wght@400;500;600&display=swap">
<style>
  :root{
    --backdrop:#b7babd;
    --green-deep:#1d7a3d;
    --green-mid:#2f9e48;
    --green-bright:#1f9a4a;
    --lime:#a6c63c;
    --lime-soft:#b5cf45;
    --ink:#2e2f31;
    --white:#ffffff;
  }
  *{box-sizing:border-box;margin:0;padding:0}
  html,body{width:929px;height:1200px;overflow:hidden}
  body{background:var(--backdrop);font-family:"Manrope",sans-serif;color:var(--ink)}
  .flyer{
    position:absolute;left:41px;top:0;width:847px;height:1200px;overflow:hidden;
    background:
      radial-gradient(ellipse at 85% 95%, #b4cf3e 0%, rgba(180,207,62,0) 55%),
      radial-gradient(ellipse at 10% 80%, #5fb043 0%, rgba(95,176,67,0) 50%),
      linear-gradient(170deg, #1d9446 0%, #24974a 45%, #6db943 75%, #a9cb3f 100%);
  }
  .brand{position:absolute;left:80px;top:150px;width:270px;text-align:center;color:var(--white);font-weight:500}
  .brand-name{font-size:50px;letter-spacing:.04em;line-height:1}
  .brand-sub{font-size:18px;letter-spacing:.22em;margin-top:6px;line-height:1}
  .photo{position:absolute;border:7px solid var(--white);box-shadow:2px 4px 10px rgba(0,0,0,.35)}
  .photo-grooves{left:364px;top:42px;width:282px;height:226px;transform:rotate(12deg);
    background:linear-gradient(135deg,#d8cfc0 0%,#9f968a 45%,#c9c0b0 70%,#7e776d 100%)}
  .photo-machine{left:606px;top:58px;width:228px;height:262px;transform:rotate(-11deg);
    background:linear-gradient(180deg,#c6d8e6 0%,#dfe6ea 30%,#5a6466 55%,#b9b7ae 100%)}
  .photo-plained{left:680px;top:628px;width:165px;height:200px;transform:rotate(-13deg);
    background:linear-gradient(160deg,#8e7a62 0%,#b4a38b 45%,#7d6b55 100%)}
  .card{position:absolute;background:var(--white);border-radius:14px 0 14px 0;overflow:hidden}
  .card-head{height:63px;display:flex;align-items:center;justify-content:center;
    font-family:"Bebas Neue",sans-serif;font-size:36px;color:var(--white);letter-spacing:.005em;padding-top:4px}
  .head-lime{background:var(--lime)}
  .head-dark{background:var(--green-deep)}
  .card-deep{left:93px;top:344px;width:317px;height:727px}
  .card-mini{left:438px;top:344px;width:316px;height:305px}
  .card-plain{left:438px;top:674px;width:316px;height:199px}
  .card-plain .card-head{justify-content:flex-start;padding-left:105px}
  .card-sensor{left:438px;top:894px;width:316px;height:177px}
  .item{position:absolute;font-size:15px;line-height:20px;letter-spacing:-.02em}
  .item svg{position:absolute;width:32px;height:32px;top:-1px}
  .card-deep .item{left:87px;width:215px}
  .card-deep .item svg{left:-64px}
  .card-side .item{left:75px;width:228px}
  .card-side .item svg{left:-54px}
  .card-plain .item{width:165px}
  .icon-lime{fill:var(--lime);stroke:var(--lime)}
  .icon-dark{fill:var(--green-deep);stroke:var(--green-deep)}
  .cow{position:absolute;left:0;top:935px;width:252px;height:250px;border-radius:40% 50% 10% 10%;
    background:linear-gradient(120deg,#f1eee8 0%,#3b2a22 35%,#efebe4 60%,#2f231d 85%)}
  .web{position:absolute;left:268px;top:1138px;width:312px;height:46px;background:var(--green-mid);
    border-radius:3px;color:var(--white);font-size:17px;font-weight:600;letter-spacing:.12em;
    display:flex;align-items:center;justify-content:center}
</style>
</head>
<body>
<main class="flyer">
  <div class="brand">
    <div class="brand-name">MARWELL</div>
    <div class="brand-sub">HERD SERVICES</div>
  </div>

  <div class="photo photo-grooves" role="img" aria-label="Close view of deep straight grooves cut into concrete"></div>
  <div class="photo photo-machine" role="img" aria-label="Grooving machine working on a concrete yard"></div>

  <section class="card card-deep">
    <h2 class="card-head head-lime">Deep Grooving</h2>
    <p class="item" style="top:100px">
      <svg viewBox="0 0 32 32" class="icon-lime"><path d="M16 3l10 4v8c0 7-5 11-10 13C11 26 6 22 6 15V7z" stroke="none"/></svg>
      Ideal for Safety &amp; Efficiency</p>
    <p class="item" style="top:177px">
      <svg viewBox="0 0 32 32" class="icon-lime"><rect x="4" y="9" width="24" height="14" rx="5" fill="none" stroke-width="3"/><circle cx="12" cy="16" r="2.5" stroke="none"/><circle cx="20" cy="16" r="2.5" stroke="none"/></svg>
      Create safe and secure flooring, cows walk without hesitation</p>
    <p class="item" style="top:262px">
      <svg viewBox="0 0 32 32" class="icon-lime"><ellipse cx="7" cy="22" rx="3" ry="6" stroke="none"/><ellipse cx="13" cy="21" rx="3" ry="6" stroke="none"/><ellipse cx="21" cy="11" rx="3" ry="6" stroke="none"/><ellipse cx="27" cy="10" rx="3" ry="6" stroke="none"/></svg>
      Achieve groove spacing for optimal hoof function, reduce hoof trauma</p>
    <p class="item" style="top:346px">
      <svg viewBox="0 0 32 32" class="icon-lime"><g stroke="none"><rect x="3" y="4" width="12" height="5"/><rect x="17" y="4" width="12" height="5"/><rect x="3" y="11" width="6" height="5"/><rect x="11" y="11" width="12" height="5"/><rect x="25" y="11" width="4" height="5"/><rect x="3" y="18" width="12" height="5"/><rect x="17" y="18" width="12" height="5"/><rect x="8" y="25" width="12" height="5"/></g></svg>
      Ideal grooves to new concrete or surfaces with little to no pattern or previous grooving</p>
    <p class="item" style="top:432px">
      <svg viewBox="0 0 32 32" class="icon-lime"><circle cx="16" cy="16" r="12" fill="none" stroke-width="3"/><path d="M10 16l4 4 8-8" fill="none" stroke-width="3.5" stroke-linecap="round" stroke-linejoin="round"/></svg>
      Ideal groove pattern as promoted by The pasturewide programme</p>
    <p class="item" style="top:516px">
      <svg viewBox="0 0 32 32" class="icon-lime"><circle cx="18" cy="11" r="8" fill="none" stroke-width="2.5"/><path d="M18 6l1.6 3.4 3.6.4-2.7 2.4.8 3.6-3.3-1.9-3.3 1.9.8-3.6-2.7-2.4 3.6-.4z" stroke="none"/><path d="M3 22h6l6 3h8l6-4v4l-7 5H3z" fill="none" stroke-width="2.5" stroke-linejoin="round"/></svg>
      Our hugely popular deep straight line grooving, long lasting, minimal hoof wear</p>
  </section>

  <section class="card card-mini card-side">
    <h2 class="card-head head-dark">Mini Grooving</h2>
    <p class="item" style="top:100px">
      <svg viewBox="0 0 32 32" class="icon-dark"><path d="M16 2v8" fill="none" stroke-width="2.5"/><path d="M16 10l8 4v8l-8 4-8-4v-8z" stroke="none"/><path d="M2 28l8-5M30 28l-8-5" fill="none" stroke-width="2.5"/></svg>
      Smaller dimensions Ideal option for heifer housing and high activity areas such as parlours and handling areas</p>
    <p class="item" style="top:204px">
      <svg viewBox="0 0 32 32" class="icon-dark"><path d="M16 3v24M6 8h20M10 29h12" fill="none" stroke-width="2.5"/><path d="M2 18l4-9 4 9zM22 18l4-9 4 9z" stroke="none"/></svg>
      An ideal solution for regaining traction on old previous grooving that has lost its traction without loosing stability</p>
  </section>

  <section class="card card-plain card-side">
    <h2 class="card-head head-lime">Plaining</h2>
    <p class="item" style="top:88px">
      <svg viewBox="0 0 32 32" class="icon-lime"><path d="M16 3c6 6 9 10 9 14a9 9 0 0 1-18 0c0-4 3-8 9-14z" stroke="none"/><rect x="14" y="24" width="4" height="7" stroke="none"/></svg>
      Smoothing down rough concrete with previous aggressive grooving or patterns to reduce hoof trauma &amp; wear</p>
  </section>

  <div class="photo photo-plained" role="img" aria-label="Concrete floor after plaining, seen from above"></div>

  <section class="card card-sensor card-side">
    <h2 class="card-head head-dark">Sensor Plate Sinking</h2>
    <p class="item" style="top:86px">
      <svg viewBox="0 0 32 32" class="icon-dark"><rect x="8" y="8" width="14" height="16" rx="3" stroke="none"/><rect x="10" y="25" width="10" height="5" stroke="none"/><circle cx="24" cy="10" r="6" fill="#fff" stroke-width="2"/><path d="M21 10l2 2 4-4" fill="none" stroke-width="2"/></svg>
      Sinking sensor plates for automated machines below surface level preventing accidental damage &amp; wear</p>
  </section>

  <div class="cow" role="img" aria-label="Black and white dairy cow standing"></div>

  <div class="web">marwellherdservices.com</div>
</main>
</body>
</html>
```